Our Hearth's Pie website

We have a new website designed and we're ready for front end design

Staging server http://staging.ourhearthspie.test which uses sparrow scaffold 3.* and we’re looking for a flat design that doesn’t go into the typical italian theme.

We need the desktop and mobile view for all of pages.

Homepage:

If you take a look at the homepage of the staging site you will notice the six boxes but we’re not interested in the Latest Chirps, but we do have a Submit Your Recipe, and Special of the Week

However we are happy with the wireframe with the logo in the middle.

This is our current site: http://crustwithelio.test so we need forest green colors.

Inner Page:

This is our staging inner page template: http://staging.ourhearthspie.test/page/2 and I imagine the links that are in the footer to also
be represented in the inner file. However;

UI Kit:

Here is the UI kit which has all the types of fields, and html doc types which we need.

http://gridkitparts.test

Order Flow:

We need the order flow for the entire buying process from the homepage to the checkout screen.

http://staging.ourhearthspie.test
http://staging.ourhearthspie.test/order
http://staging.ourhearthspie.test/menu
http://staging.ourhearthspie.test/customize/2

Things to think about:

How will we offer upsells
We want to have a pizza builder https://order.dovecrust.test/site/pizza/builder

Target Market(s)

Pizza lovers

Industry/Entity Type

Builder

Font styles to use
Sans Serif

Colors
9bcb3c

Requirements
Must have
• Call to Action to Order a pizza.
neat / layered *.psd or *.fw.png
WEB SAFE FONTS! We like lumen fonts.
scaffolds 960 grid
UX
Nice to have
• Integrating sacred geometry creatively and very subtle. Needing new logo meshed with old logo, must talk to you about this
Should not have
• Complicated Backgrounds with gradients. We like flat design.
Typical Italian Theme
Sliders.

```html
<!DOCTYPE html>
<html lang="en">
<head>
<meta charset="utf-8">
<title>About — Our Hearth's Pie</title>
<link href="https://fonts.googleapis.com/css2?family=Roboto:wght@300;400&display=swap" rel="stylesheet">
<style>
  :root{
    --forest:#2a925a;
    --forest-dark:#1f7a48;
    --lime:#b7e06a;
    --lime-btn:#9bcb3c;
    --red:#e0252c;
    --ink:#333333;
    --muted:#555555;
    --rule:#8a8a8a;
    --dots:#bbbbbb;
    --scallop:#cfe6d6;
    --paper:#ffffff;
  }
  *{box-sizing:border-box;margin:0;padding:0}
  html,body{width:1200px;height:1023px;overflow:hidden;background:var(--paper)}
  body{position:relative;font-family:'Roboto',sans-serif;font-weight:300;color:var(--ink)}
  .abs{position:absolute}
  a{color:inherit;text-decoration:none}

  .top-band{left:0;top:0;width:1200px;height:14px;background:var(--scallop)}

  .brand{left:70px;top:52px;display:flex;align-items:center;gap:14px}
  .brand-dot{width:18px;height:18px;border-radius:50%;background:var(--forest)}
  .brand-name{font-size:30px;font-weight:400;color:var(--forest);white-space:nowrap}
  .brand-tag{left:102px;top:90px;font-size:15px;color:var(--forest);font-weight:400}

  .account{right:66px;top:51px;display:flex;align-items:center;gap:6px;font-size:13px;font-weight:400}
  .account .cart{margin-right:2px;color:var(--ink)}
  .btn-login,.btn-signup{height:22px;padding:0 14px;color:#fff;font-size:13px;display:flex;align-items:center}
  .btn-login{background:var(--forest)}
  .btn-signup{background:var(--lime-btn)}
  .social{width:23px;height:23px}
  .social.one{background:#3a9bd8}
  .social.two{background:#3b5a98}

  .main-nav{right:66px;top:88px;display:flex;font-size:16px;font-weight:400;color:var(--muted)}
  .main-nav a+a::before{content:"/";color:#bbb;margin:0 10px}
  .main-nav .current{color:var(--forest)}

  .double-rule{border-top:1px solid var(--rule);border-bottom:1px solid var(--rule);height:4px}

  .menu-head{left:82px;top:172px;display:flex;align-items:center;gap:12px}
  .menu-head h2{font-size:29px;font-weight:300;color:var(--ink)}
  .dotted{border-top:1px dotted var(--dots)}

  .cat{left:82px;width:280px;height:32px;background:var(--forest);color:#fff;font-size:18px;padding-left:10px;display:flex;align-items:center}
  .cat::before{content:"-";margin-right:9px}
  .cat-list{left:82px;top:279px;width:280px;height:172px;background:var(--lime);padding:6px 0 0 10px;display:grid;grid-template-columns:119px 1fr;grid-auto-rows:22.5px;font-size:13px;font-weight:400;color:#222}

  .page-title{left:405px;top:180px;font-size:30px;font-weight:300;color:var(--forest)}
  .order-btn{left:946px;top:175px;width:187px;height:42px;background:var(--red);color:#fff;font-size:18px;font-weight:400;display:flex;align-items:center;justify-content:center;gap:8px}

  .copy{left:405px;width:729px;font-size:14px;line-height:18.75px;color:#333}
  .hero-frame{left:405px;top:387px;width:729px;height:175px;border:1px solid #ccc;padding:3px;background:#fff}
  .hero-fill{width:100%;height:100%;background:linear-gradient(90deg,#8a96a4 0%,#b9a99a 40%,#5f8aa8 62%,#c7a28a 78%,#c9432a 92%,#e07b3a 100%)}

  .divider{width:0;border-left:1px dotted #999}
  .col-head{display:flex;align-items:center;gap:10px;font-size:24px;color:var(--forest);font-weight:400}
  .col-text{font-size:14.5px;line-height:18px;color:#333}
  .col-text p+p{margin-top:4px}

  .specials-frame{left:451px;top:796px;width:298px;height:103px;border:1px solid #ddd;padding:3px;box-shadow:0 1px 3px rgba(0,0,0,.15)}
  .specials-fill{width:100%;height:100%;background:linear-gradient(120deg,#e6b07a,#c4542c 50%,#e9c27a)}
  .weekly-card{left:816px;top:794px;width:298px;height:104px;border:1px solid #ddd;box-shadow:0 1px 3px rgba(0,0,0,.15);background:#fff}
  .weekly-card h4{position:absolute;left:9px;top:10px;font-size:18px;font-weight:400;color:var(--forest)}
  .weekly-card p{position:absolute;left:11px;top:36px;width:125px;font-size:12px;line-height:15.5px;color:#444}
  .weekly-pie{position:absolute;right:4px;top:3px;width:160px;height:96px;border-radius:50%;background:radial-gradient(circle,#d65a34 0%,#c9432a 55%,#e9b676 75%,#fff 76%)}

  .footer-brand{left:500px;top:938px;width:200px;text-align:center;font-size:17px;font-weight:400;color:var(--forest)}
  .footer-links{left:66px;top:969px;font-size:14.5px;font-weight:300;color:#333}
  .footer-copy{right:66px;top:969px;font-size:14.5px;color:#333}
</style>
</head>
<body>

<div class="abs top-band" role="img" aria-label="Row of small patterned circles along the page top"></div>

<header>
  <div class="abs brand"><span class="brand-dot"></span><span class="brand-name">Our Hearth's Pie</span></div>
  <div class="abs brand-tag">Serving Dallas since 1956</div>

  <div class="abs account">
    <span class="cart">Items (0) | Total: 0.00 | Checkout</span>
    <a class="btn-login" href="#">Login</a>
    <a class="btn-signup" href="#">Signup</a>
    <span class="social one"></span>
    <span class="social two"></span>
  </div>

  <nav class="abs main-nav">
    <a class="current" href="#">Home</a><a href="#">Locations</a><a href="#">Order Online</a><a href="#">Menu</a><a href="#">Contact Us</a><a href="#">About</a>
  </nav>
</header>

<div class="abs double-rule" style="left:66px;top:136px;width:1068px"></div>

<aside>
  <div class="abs menu-head">
    <svg width="36" height="44" viewBox="0 0 36 44" aria-hidden="true">
      <rect x="2" y="2" width="30" height="38" fill="#555"/>
      <rect x="8" y="10" width="16" height="3" fill="#fff"/>
      <rect x="8" y="17" width="16" height="3" fill="#fff"/>
      <rect x="8" y="24" width="12" height="3" fill="#fff"/>
      <path d="M22 30 h10 v14 l-5 -4 l-5 4z" fill="#2a925a"/>
    </svg>
    <h2>Our Menu</h2>
  </div>
  <div class="abs dotted" style="left:82px;top:232px;width:296px"></div>

  <div class="abs cat" style="top:247px">Speciality Pizzas</div>
  <div class="abs cat-list">
    <span>- Greek</span><span>- Full Moon</span>
    <span>- Caligula</span><span>- Greek</span>
    <span>- Augustus</span><span>- BBQ chicken</span>
    <span>- Chicken Veggie</span><span>- Chicken/Bacon/Ranch</span>
    <span>- Margherita</span><span>- Chicken Parmesan</span>
    <span>- Veggie</span><span>- Maximus</span>
    <span>- Meathead</span><span></span>
  </div>
  <div class="abs cat" style="top:463px">Appetizers</div>
  <div class="abs cat" style="top:509px">Salads</div>
  <div class="abs cat" style="top:554px">Pastas</div>
  <div class="abs cat" style="top:599px">Deserts</div>
  <div class="abs cat" style="top:644px">Calzones</div>
</aside>

<main>
  <h1 class="abs page-title">About Our Hearth's Pie</h1>
  <a class="abs order-btn" href="#">
    <svg width="24" height="24" viewBox="0 0 24 24" aria-hidden="true">
      <rect x="2" y="2" width="16" height="20" fill="none" stroke="#fff" stroke-width="2"/>
      <path d="M6 8h8M6 12h8M6 16h5" stroke="#fff" stroke-width="2"/>
      <path d="M14 18 L22 6" stroke="#fff" stroke-width="3"/>
    </svg>
    ORDER ONLINE
  </a>
  <div class="abs dotted" style="left:405px;top:232px;width:729px"></div>

  <p class="abs copy" style="top:245px">Our family roots reach back to the harbor town of Palermo, Sicily.&nbsp; Harbor town life provided our family a hard-working existence and a passion for simple, but really good food.&nbsp; Our family immigrated to America in the early 1900s and after living in New York and Kansas City, decided on settling in Dallas in the early 1940s.&nbsp; My father opened up the Halvard Lounge in the late forty's and started serving his mothers pizza shortly thereafter. After seeing how popular the pizza was, he decided to convert the lounge into a pizzeria in 1956, becoming the first true "pizzeria" in the city.&nbsp; With city expansion booming in the early 1960s, my father decided to move to the farthest part of Dallas which then was Brennor Road intersecting Corwin Lane; construction on the Loop had just begun.</p>

  <div class="abs hero-frame"><div class="hero-fill" role="img" aria-label="Harbor town panorama with mountains beside a freshly baked pizza"></div></div>

  <p class="abs copy" style="top:584px">Lorem Ipsum is simply dummy text of the printing and typesetting industry. Lorem Ipsum has been the industry's standard dummy text ever since the 1500s, when an unknown printer took a galley of type and scrambled it to make a type specimen book. It has survived not only five centuries, but also the leap into electronic typesetting, remaining essentially unchanged. It was popularised in the 1960s with the release of Lettersheet sheets containing Lorem Ipsum passages, and more recently with desktop publishing software like Folio PageSetter including versions of Lorem Ipsum.</p>
</main>

<div class="abs dotted" style="left:66px;top:723px;width:1068px"></div>

<section>
  <div class="abs col-head" style="left:82px;top:754px">
    <svg width="64" height="32" viewBox="0 0 64 32" aria-hidden="true">
      <rect x="2" y="3" width="26" height="26" fill="#c9262b"/>
      <circle cx="48" cy="16" r="13" fill="none" stroke="#e0252c" stroke-width="3"/>
      <path d="M41 16 l5 5 l9 -10" fill="none" stroke="#e0252c" stroke-width="3"/>
    </svg>
    Recent Accolades
  </div>
  <div class="abs col-text" style="left:83px;top:797px;width:322px">
    <p>Since 1956, we've been honored as having the best pizza in Dallas</p>
    <p>Dallas and Wingline News awarded us the best pizza in Dallas for 2010 as a finalist in Metro Table Magazine this year</p>
  </div>
  <div class="abs divider" style="left:415px;top:756px;height:158px"></div>

  <div class="abs col-head" style="left:453px;top:745px">
    <svg width="46" height="42" viewBox="0 0 46 42" aria-hidden="true">
      <path d="M4 26 L30 8 L40 30 L12 34 Z" fill="#555"/>
      <path d="M30 8 L40 30" stroke="#333" stroke-width="3"/>
      <rect x="14" y="33" width="6" height="8" fill="#555"/>
    </svg>
    Specials of the week
  </div>
  <div class="abs specials-frame"><div class="specials-fill" role="img" aria-label="Hands reaching for slices of a shared pizza"></div></div>
  <div class="abs divider" style="left:784px;top:756px;height:158px"></div>

  <div class="abs col-head" style="left:816px;top:745px">
    <svg width="42" height="42" viewBox="0 0 42 42" aria-hidden="true">
      <path d="M10 4 h22 v10 a11 11 0 0 1 -22 0z" fill="#555"/>
      <path d="M10 8 h-6 a8 8 0 0 0 8 10 M32 8 h6 a8 8 0 0 1 -8 10" fill="none" stroke="#555" stroke-width="3"/>
      <rect x="18" y="24" width="6" height="8" fill="#555"/>
      <rect x="12" y="32" width="18" height="6" fill="#555"/>
    </svg>
    Week Customer Specials
  </div>
  <div class="abs weekly-card">
    <h4>Chicken Veggie</h4>
    <p>Organic chicken, red onions, black olives, roma tomatoes &amp; fresh basil</p>
    <div class="weekly-pie" role="img" aria-label="Chicken veggie pizza topped with olives and tomatoes"></div>
  </div>
</section>

<footer>
  <div class="abs double-rule" style="left:66px;top:954px;width:409px"></div>
  <div class="abs double-rule" style="left:680px;top:954px;width:454px"></div>
  <div class="abs footer-brand">Our Hearth's Pie</div>
  <div class="abs footer-links"><a href="#">Gift Card</a> | <a href="#">Newsletter</a> | <a href="#">Coupons</a> | <a href="#">Jobs</a> | <a href="#">Specials</a></div>
  <div class="abs footer-copy">@2014 Our Hearth's Pie, All Rights Reserved</div>
</footer>

</body>
</html>
```